Brisk Meadow LLC business card

I created a front and back idea of what I want. Also I included my Brisk Meadow logo to be used on the card. Please use your creativity to make it look professional and awesome! Use the all text and phrases in the sample card that I made.

(Front of card)Key words and phrases:
FOOD GROWING MACHINES
Aeroponics Technology
No soil
No pesticides
98% less water
Grow year round

(Back of card)
EVERY MONTH ONE PILLAR PLOT WILL BE GIVEN AWAY
FOLLOW US ON IG FOR A CHANCE TO WIN A PILLAR PLOT
FOOD GROWING MACHINES
Vertical Farming
Urban Farming
100% Organic
Grows 40% Faster
Indoors/outdoors

My contact info:
Chef Rulo
Phone:415 372-8491
web: briskmeadow.example
IG: briskmeadowvx

Target Market(s)

urban farming, vertical farming gardening

Industry/Entity Type

Gardening

Contact Information for Business Card

Front of card)Key words and phrases:
FOOD GROWING MACHINES
Aeroponics Technology
No soil
No pesticides
98% less water
Grow year round

(Back of card)
FOOD GROWING MACHINES
Vertical Farming
Urban Farming
100% Organic
Grows 40% Faster
Indoors/outdoors

My contact info:
Phone:415 372-8491
web: briskmeadow.example
IG: briskmeadowvx

Requirements
Must have
• My contact info:
Chef Rulo
Phone:415 372-8491
web: briskmeadow.example
IG: briskmeadowvx
Nice to have
• Great imagery and easy to read. Try to incorporate the image that I uploaded of the little girl.

```html
<!DOCTYPE html>
<html lang="en">
<head>
<meta charset="utf-8">
<title>Brisk Meadow LLC – Business Cards</title>
<link rel="stylesheet" href="https://fonts.googleapis.com/css2?family=Roboto:ital,wght@0,400;0,500;0,700;0,900;1,700;1,900&display=swap">
<style>
  :root{
    --navy:#1b2540;
    --green:#8dc63f;
    --white:#ffffff;
    --page:#e9e9ea;
  }
  *{box-sizing:border-box;margin:0;padding:0}
  html,body{width:1200px;height:1200px;overflow:hidden;background:var(--page)}
  body{position:relative;font-family:'Roboto',Arial,sans-serif}

  .card{
    position:absolute;left:219px;width:952px;height:638px;
    transform:scale(.8);transform-origin:top left;
    background:var(--navy);overflow:hidden;
  }
  .card--front{top:50px}
  .card--back{top:623px}

  .card__art{position:absolute;left:0;top:0;width:952px;height:466px}

  .brand{
    position:absolute;color:var(--green);font-weight:900;
    font-size:50px;line-height:44px;letter-spacing:1px;text-transform:uppercase;
  }
  .card--front .brand{left:61px;top:96px}
  .card--back .brand{left:46px;top:50px}
  .brand__dot{
    display:inline-block;width:22px;height:22px;border-radius:50%;
    background:var(--green);margin-left:8px;vertical-align:middle;
  }

  .checks{position:absolute;list-style:none;color:var(--white);font-size:24px}
  .checks li{display:flex;align-items:center;height:42px}
  .checks svg{width:22px;height:22px;margin-right:12px;flex:none}
  .card--front .checks{left:60px;top:214px}
  .card--back .checks{left:46px;top:314px;font-size:22px}
  .card--back .checks li{height:41px}
  .card--back .checks svg{margin-right:8px}

  .giveaway{
    position:absolute;left:46px;top:150px;color:var(--white);
    font-size:23px;line-height:30px;text-transform:uppercase;font-weight:500;
  }
  .giveaway__accent{color:var(--green);font-style:italic;font-weight:900}
  .giveaway__accent--big{font-size:27px;line-height:36px}

  .band{
    position:absolute;left:0;top:466px;width:952px;height:79px;
    background:var(--green);display:flex;align-items:center;
  }
  .band__title{
    margin-left:43px;color:var(--navy);font-weight:700;font-size:46px;letter-spacing:-.3px;
  }
  .band__pill{
    position:absolute;left:675px;top:8px;width:237px;height:66px;border-radius:14px;
    background:linear-gradient(180deg,#ffffff 10%,#c9e59d 100%);
    color:var(--navy);font-size:24px;line-height:25px;font-weight:500;
    display:flex;flex-direction:column;justify-content:center;padding-left:34px;
  }

  .contact{
    position:absolute;left:0;top:545px;width:952px;height:93px;
    display:flex;align-items:center;justify-content:center;gap:16px;
    color:var(--white);font-size:25px;font-weight:500;padding-bottom:14px;
  }
  .contact__name{color:var(--green);font-style:italic;font-weight:700}
  .contact__item{display:flex;align-items:center;gap:6px}
  .contact__item svg{width:22px;height:22px;flex:none}
  .contact__square{width:22px;height:22px;border:2.5px solid var(--green);border-radius:5px;flex:none}
</style>
</head>
<body>

<!-- FRONT -->
<section class="card card--front">
  <svg class="card__art" viewBox="0 0 952 466">
    <defs>
      <linearGradient id="photoTones" x1="0" y1="0" x2="1" y2="0">
        <stop offset="0" stop-color="#6e5446"/>
        <stop offset=".32" stop-color="#a05a7c"/>
        <stop offset=".5" stop-color="#8e735f"/>
        <stop offset=".6" stop-color="#b9b3a8"/>
        <stop offset=".7" stop-color="#78a84c"/>
        <stop offset="1" stop-color="#4e8a2e"/>
      </linearGradient>
      <linearGradient id="photoShade" x1="0" y1="0" x2="0" y2="1">
        <stop offset="0" stop-color="#000" stop-opacity=".12"/>
        <stop offset=".5" stop-color="#000" stop-opacity="0"/>
        <stop offset="1" stop-color="#000" stop-opacity=".18"/>
      </linearGradient>
    </defs>
    <g role="img" aria-label="Photo of a girl holding a colander beside a vertical aeroponic tower growing chard">
      <path d="M460 0H952V466H262C385 385 460 210 460 0Z" fill="url(#photoTones)"/>
      <path d="M460 0H952V466H262C385 385 460 210 460 0Z" fill="url(#photoShade)"/>
    </g>
    <path d="M436 0C436 210 356 385 228 466H262C385 385 460 210 460 0Z" fill="var(--green)"/>
  </svg>

  <div class="brand">Brisk<span class="brand__dot"></span><br>Meadow</div>

  <ul class="checks">
    <li><svg viewBox="0 0 24 24"><path d="M3 13l6 6L21 5" fill="none" stroke="#8dc63f" stroke-width="4" stroke-linecap="round" stroke-linejoin="round"/></svg>No soil</li>
    <li><svg viewBox="0 0 24 24"><path d="M3 13l6 6L21 5" fill="none" stroke="#8dc63f" stroke-width="4" stroke-linecap="round" stroke-linejoin="round"/></svg>No pesticides</li>
    <li><svg viewBox="0 0 24 24"><path d="M3 13l6 6L21 5" fill="none" stroke="#8dc63f" stroke-width="4" stroke-linecap="round" stroke-linejoin="round"/></svg>98% less water</li>
    <li><svg viewBox="0 0 24 24"><path d="M3 13l6 6L21 5" fill="none" stroke="#8dc63f" stroke-width="4" stroke-linecap="round" stroke-linejoin="round"/></svg>Grow year round</li>
  </ul>

  <div class="band">
    <span class="band__title">FOOD GROWING MACHINES</span>
    <div class="band__pill"><span>Aeroponics</span><span>Technology</span></div>
  </div>

  <div class="contact">
    <span class="contact__name">Chef Rulo</span>
    <span class="contact__item"><svg viewBox="0 0 24 24"><path d="M6.6 10.8a15.1 15.1 0 006.6 6.6l2.2-2.2c.3-.3.7-.4 1-.2 1.1.4 2.3.6 3.6.6.6 0 1 .4 1 1V20c0 .6-.4 1-1 1A17 17 0 013 4c0-.6.4-1 1-1h3.5c.6 0 1 .4 1 1 0 1.3.2 2.5.6 3.6.1.3 0 .7-.2 1z" fill="#8dc63f"/></svg>415 372-8491</span>
    <span class="contact__item"><svg viewBox="0 0 24 24" fill="none" stroke="#8dc63f" stroke-width="2"><circle cx="12" cy="12" r="9.5"/><ellipse cx="12" cy="12" rx="4.5" ry="9.5"/><path d="M2.5 12h19M4 7h16M4 17h16"/></svg>briskmeadow.example</span>
    <span class="contact__item"><span class="contact__square"></span>briskmeadowvx</span>
  </div>
</section>

<!-- BACK -->
<section class="card card--back">
  <svg class="card__art" viewBox="0 0 952 466">
    <defs>
      <linearGradient id="photoTonesBack" x1="0" y1="0" x2="1" y2="0">
        <stop offset="0" stop-color="#6e5446"/>
        <stop offset=".32" stop-color="#a05a7c"/>
        <stop offset=".5" stop-color="#8e735f"/>
        <stop offset=".6" stop-color="#b9b3a8"/>
        <stop offset=".7" stop-color="#78a84c"/>
        <stop offset="1" stop-color="#4e8a2e"/>
      </linearGradient>
      <linearGradient id="photoShadeBack" x1="0" y1="0" x2="0" y2="1">
        <stop offset="0" stop-color="#000" stop-opacity=".12"/>
        <stop offset=".5" stop-color="#000" stop-opacity="0"/>
        <stop offset="1" stop-color="#000" stop-opacity=".18"/>
      </linearGradient>
    </defs>
    <g role="img" aria-label="Photo of a girl holding a colander beside a vertical aeroponic tower growing chard">
      <path d="M460 0H952V466H262C385 385 460 210 460 0Z" fill="url(#photoTonesBack)"/>
      <path d="M460 0H952V466H262C385 385 460 210 460 0Z" fill="url(#photoShadeBack)"/>
    </g>
    <path d="M436 0C436 210 356 385 228 466H262C385 385 460 210 460 0Z" fill="var(--green)"/>
  </svg>

  <div class="brand">Brisk<span class="brand__dot"></span><br>Meadow</div>

  <p class="giveaway">
    Every month one Pillar Plot<br>
    will be given away<br>
    <span class="giveaway__accent">Follow us on IG</span><br>
    for a chance to<br>
    <span class="giveaway__accent giveaway__accent--big">Win a Pillar Plot</span>
  </p>

  <ul class="checks">
    <li><svg viewBox="0 0 24 24"><path d="M3 13l6 6L21 5" fill="none" stroke="#8dc63f" stroke-width="4" stroke-linecap="round" stroke-linejoin="round"/></svg>100% Organic</li>
    <li><svg viewBox="0 0 24 24"><path d="M3 13l6 6L21 5" fill="none" stroke="#8dc63f" stroke-width="4" stroke-linecap="round" stroke-linejoin="round"/></svg>Grows 40% Faster</li>
    <li><svg viewBox="0 0 24 24"><path d="M3 13l6 6L21 5" fill="none" stroke="#8dc63f" stroke-width="4" stroke-linecap="round" stroke-linejoin="round"/></svg>Indoors/outdoors</li>
  </ul>

  <div class="band">
    <span class="band__title">FOOD GROWING MACHINES</span>
    <div class="band__pill"><span>Vertical Farming</span><span>Urban Farming</span></div>
  </div>

  <div class="contact">
    <span class="contact__name">Chef Rulo</span>
    <span class="contact__item"><svg viewBox="0 0 24 24"><path d="M6.6 10.8a15.1 15.1 0 006.6 6.6l2.2-2.2c.3-.3.7-.4 1-.2 1.1.4 2.3.6 3.6.6.6 0 1 .4 1 1V20c0 .6-.4 1-1 1A17 17 0 013 4c0-.6.4-1 1-1h3.5c.6 0 1 .4 1 1 0 1.3.2 2.5.6 3.6.1.3 0 .7-.2 1z" fill="#8dc63f"/></svg>415 372-8491</span>
    <span class="contact__item"><svg viewBox="0 0 24 24" fill="none" stroke="#8dc63f" stroke-width="2"><circle cx="12" cy="12" r="9.5"/><ellipse cx="12" cy="12" rx="4.5" ry="9.5"/><path d="M2.5 12h19M4 7h16M4 17h16"/></svg>briskmeadow.example</span>
    <span class="contact__item"><span class="contact__square"></span>briskmeadowvx</span>
  </div>
</section>

</body>
</html>
```